Facebook Advert for caravan storage & Caravan sales products

We are Pellowdene Leisure.

History about us!!
Pellowdene store close to 300 touring caravans in Cornwall UK, We also sell caravans by buying & selling ourselves or via our brokerage service. Pellowdene also has a small Caravan park.

What i want
I would like a Bold advert designed that can be placed on my facebook page & also on a series of Facebook selling groups. I would like my logo on it also the cartoon picture of me.

Make sure you point out we are based in Cornwall, I would like the following somewhere on the advert.

The brokerage advantages: can help arrange finance, we can take px back against your caravan, Let us sell your caravan, List of waiting buyers, Free storage while its up for sale. (do not just copy this please shorten it for an advert, mix it up if you have to)

Please also try put somewhere "We buy caravans" transport available
& secure storage available, 01347 62814 www.pellowdeneleisure.example.co.uk

Target Market(s)

People looking to sell or buy touring caravans

Colors

Designer to choose colors to be used in the design.

Requirements
Must have
• Colour
• Boldness
• Bright
• To the point

```html
<!DOCTYPE html>
<html lang="en">
<head>
<meta charset="utf-8">
<title>Pellowdene Leisure – Buy, Sell and Brokerage Service</title>
<link rel="stylesheet" href="https://fonts.googleapis.com/css2?family=Anton&family=Arimo:wght@400;700&display=swap">
<style>
  :root {
    --sky: #3fb3e6;
    --sky-deep: #2a9fd8;
    --band: #29a8e0;
    --pale: #d8edf8;
    --white: #ffffff;
    --ink: #111111;
    --grey: #5b5b5b;
    --link: #2aa6df;
  }
  * { margin: 0; padding: 0; box-sizing: border-box; }
  html, body { width: 848px; height: 1200px; overflow: hidden; background: var(--white); }
  .advert {
    position: relative;
    width: 848px;
    height: 1200px;
    overflow: hidden;
    font-family: "Arimo", Arial, sans-serif;
    background:
      radial-gradient(circle at 110px 120px, rgba(255,255,255,.25) 0 60px, transparent 61px),
      radial-gradient(circle at 250px 140px, rgba(255,255,255,.18) 0 45px, transparent 46px),
      radial-gradient(circle at 640px 110px, rgba(255,255,255,.2) 0 55px, transparent 56px),
      radial-gradient(circle at 170px 470px, rgba(255,255,255,.12) 0 70px, transparent 71px),
      radial-gradient(circle at 560px 560px, rgba(255,255,255,.1) 0 90px, transparent 91px),
      radial-gradient(circle at 300px 690px, rgba(255,255,255,.1) 0 85px, transparent 86px),
      radial-gradient(circle at 700px 640px, rgba(255,255,255,.08) 0 80px, transparent 81px),
      linear-gradient(180deg, #66c4ef 0, #45b3e6 187px, var(--sky-deep) 188px, var(--sky) 600px, #48b8e9 980px);
  }
  .advert::before {
    content: "";
    position: absolute;
    inset: 0 0 auto 0;
    height: 187px;
    background: linear-gradient(90deg, rgba(255,255,255,.2), rgba(255,255,255,0) 60%, rgba(30,90,130,.25));
  }
  .footer-panel {
    position: absolute;
    left: 0; top: 980px;
    width: 848px; height: 220px;
    background: var(--pale);
  }
  .brand-disc {
    position: absolute;
    left: 267px; top: 30px;
    width: 314px; height: 314px;
    border-radius: 50%;
    background: var(--white);
    border: 3px solid var(--band);
    display: flex; flex-direction: column; align-items: center; justify-content: center;
  }
  .brand-dot {
    width: 80px; height: 80px;
    border-radius: 50%;
    background: var(--band);
    margin-bottom: 30px;
  }
  .brand-name {
    font-weight: 700;
    font-size: 27px;
    color: var(--grey);
    letter-spacing: -0.5px;
  }
  .brand-tagline {
    display: flex; align-items: center; gap: 6px;
    margin-top: 4px;
    font-size: 18px;
    color: var(--band);
  }
  .brand-tagline::before, .brand-tagline::after {
    content: ""; width: 20px; height: 2px; background: var(--band);
  }
  .service-band {
    position: absolute;
    left: 0; top: 358px;
    width: 848px; height: 70px;
    background: var(--band);
    color: var(--white);
    font-family: "Anton", Impact, sans-serif;
    font-size: 50px;
    line-height: 70px;
    text-align: center;
    letter-spacing: 0.3px;
  }
  .advantages {
    position: absolute;
    left: 0; top: 446px;
    width: 848px;
    text-align: center;
    color: var(--ink);
    font-weight: 700;
    list-style: none;
  }
  .advantages-title { font-size: 35px; line-height: 44px; letter-spacing: .5px; }
  .advantage { font-size: 24px; line-height: 48px; position: relative; }
  .advantage::before {
    content: "";
    position: absolute;
    left: 418px; top: -5px;
    width: 12px; height: 12px;
    border-radius: 50%;
    background: var(--white);
  }
  .advantage-list { list-style: none; margin-top: 11px; }
  .region {
    position: absolute;
    left: 0; top: 722px;
    width: 848px;
    text-align: center;
    font-family: "Anton", Impact, sans-serif;
    font-size: 44px;
    color: var(--white);
  }
  .badge {
    position: absolute;
    width: 180px; height: 180px;
    border-radius: 50%;
    background: var(--band);
    border: 4px solid var(--white);
    display: flex; align-items: center; justify-content: center;
    text-align: center;
    font-family: "Anton", Impact, sans-serif;
    color: var(--white);
    font-size: 32px;
    line-height: 34px;
  }
  .badge span { display: block; }
  .badge-buy { left: 51px; top: 703px; }
  .badge-buy .badge-text { transform: rotate(-8deg); }
  .badge-storage { left: 616px; top: 703px; }
  .badge-storage .badge-text { transform: rotate(8deg); }
  .media {
    position: absolute;
    width: 176px; height: 176px;
    border-radius: 50%;
    border: 4px solid var(--band);
  }
  .media-left { left: 116px; top: 892px; background: linear-gradient(160deg, #8fb9d8, #e9edf0 45%, #b9c2c8 70%, #5f8f3a); }
  .media-owner { left: 336px; top: 889px; background: radial-gradient(circle at 40% 35%, #f4fbff, #bfe3f5 60%, #7cc6ea); }
  .media-right { left: 556px; top: 892px; background: linear-gradient(160deg, #c9d3dc, #f1f3f4 45%, #d9dcdf 70%, #5d8a36); }
  .address {
    position: absolute;
    left: 0; top: 1101px;
    width: 848px;
    text-align: center;
    font-size: 18px;
    color: var(--ink);
  }
  .sep { color: var(--link); margin: 0 4px; }
  .contact {
    position: absolute;
    left: 0; top: 1132px;
    width: 848px;
    display: flex; justify-content: center; gap: 48px;
    font-weight: 700;
    font-size: 22px;
    color: var(--link);
  }
</style>
</head>
<body>
<main class="advert">
  <div class="footer-panel"></div>

  <header class="brand-disc">
    <div class="brand-dot"></div>
    <div class="brand-name">Pellowdene Leisure</div>
    <div class="brand-tagline">caravan sales &amp; storage</div>
  </header>

  <h1 class="service-band">BUY, SELL AND BROKERAGE SERVICE</h1>

  <section class="advantages">
    <h2 class="advantages-title">THE BROKERAGE ADVANTAGES:</h2>
    <ul class="advantage-list">
      <li class="advantage">• CAN HELP ARRANGE FINANCE</li>
      <li class="advantage">• WE CAN TAKE PX BACK AGAINST YOUR CARAVAN</li>
      <li class="advantage">• WE HAVE BUYERS WAITING</li>
      <li class="advantage">• FREE STORAGE WHILE YOU WAIT FOR A BUYER</li>
    </ul>
  </section>

  <p class="region">• CORNWALL •</p>

  <div class="badge badge-buy"><div class="badge-text"><span>WE</span><span>BUY</span><span>CARAVANS</span></div></div>
  <div class="badge badge-storage"><div class="badge-text"><span>SECURE</span><span>STORAGE</span><span>AVAILABLE</span></div></div>

  <div class="media media-left" role="img" aria-label="Photo of a modern white touring caravan on grass"></div>
  <div class="media media-owner" role="img" aria-label="Cartoon illustration of the owner giving a thumbs up"></div>
  <div class="media media-right" role="img" aria-label="Photo of a white touring caravan parked on grass"></div>

  <p class="address">Pellowdene Storage<span class="sep">•</span>Treventon<span class="sep">•</span>Lanmorrow<span class="sep">•</span>Cornwall<span class="sep">•</span>PL99 4ZX</p>
  <p class="contact"><span>www.pellowdeneleisure.example.co.uk</span><span>01347 62814</span></p>
</main>
</body>
</html>
```